The Velvet Easel Co - Photos to Custom Oil Paintings

We need a website and logo designed and built allowing customers to purchase custom oil paintings. The paintings will come from a customers single photograph or even combination of photos. They will be able to complete a straight forward checkout process, selecting their desired medium (oil or charcoal painting), their desired size, the number of figures in the painting, the type of background required (as per photo or let the artist decide). Which will then automaticaly provide the customer with a price for the purchase. Allowing them to add a photo to the order which they can then submit with the order present in their personal account etc etc etc.
Theres one website in particular that i will be competing with. That is based in the US - http://www.brushmyworld.example
I wish to far exceed the appearence of the already present site.
At the moment i wish to include Coinvale in the payment process. Unless there are some cheaper, more cost efficient ways, please let me know.
The company name is The Velvet Easel Co. Domain has been purchased - www.velveteasel.example (via Hostmoor - Linux)
I have no great sense of design, but the site must be straight forward, eye catching, engaging and give the customer a sense of high quality. Some kind of flash animation with pictures on the front page scrolling?
For myself, the admin side, ideally must be straight forward to maintain. The ability to update customers accounts with info (they will then be informed there is an update in their account etc)
The ability for automated emails from point of sale (sales orders with generated order numbers) to myself. Again automated emails to the customers once the "status" of their order or other information has been submitted to their account (by myself) or a similar system.
Updates
All,
Please note, the budget is able to increase subject to what additional work is needed. As far as the admin area goes. I am open to suggestions to ensure ease of use and efficiency.
Any questions, comments or ideas are fully welcomed.
Many thanks,
Daniel Pruitt
Industry/Entity Type
It Company
Logo styles of interest
Pictorial/Combination Logo
Abstract Logo
Wordmark Logo
Lettermark Logo
Look and feel
Each slider illustrates characteristics of the customer's brand and the style your logo design should communicate.

```html
<!DOCTYPE html>
<html lang="en">
<head>
<meta charset="utf-8">
<title>The Velvet Easel Co</title>
<link href="https://fonts.googleapis.com/css2?family=Open+Sans:ital,wght@0,400;0,600;1,400&family=Great+Vibes&display=swap" rel="stylesheet">
<style>
:root{
  --teal:#15958f;--teal-light:#2cb5ae;--teal-dark:#0c7b76;
  --sand:#ebe5d4;--cream:#f8f4e7;--panel:#ece6d6;--panel-dark:#e2dbc8;
  --ink:#333;--text:#4a4a4a;--muted:#7a7a7a;--red:#9a1b1b;
  --footer:#3a3938;--footer-deep:#2c2b2a;--footer-text:#d8d8d8;
}
*{margin:0;padding:0;box-sizing:border-box}
html,body{width:828px;height:1200px;overflow:hidden}
body{position:relative;background:var(--cream);font-family:"Open Sans",Arial,sans-serif;color:var(--text)}
.abs{position:absolute}
.top-band{left:0;top:0;width:828px;height:350px;background:var(--sand);border-bottom:1px solid #ddd5c0}
.ribbon{left:60px;top:18px;width:752px;height:46px}
.logo-mark{left:16px;top:10px;width:62px;height:56px;border-radius:50%;background:#efe7d3;border:2px solid #cfc3a6}
.logo-name{left:86px;top:24px;font-size:23px;font-weight:600;color:#fff;letter-spacing:.2px}
.nav a{position:absolute;top:18px;height:46px;line-height:46px;color:#fff;font-size:13px;text-decoration:none}
.nav .active{background:var(--teal-light);padding:0 18px;left:323px}
.quick-list{list-style:none}
.quick-list li{position:absolute;font-size:12.5px;color:var(--muted);padding-left:17px}
.quick-list li::before{content:"";position:absolute;left:0;top:5px;width:5px;height:5px;border-right:1.5px solid #777;border-top:1.5px solid #777;transform:rotate(45deg)}
.quick-list li.current{color:var(--ink)}
.upload{left:35px;top:236px;width:256px;height:55px;border-radius:5px;background:linear-gradient(#ddd6c5,#cdc5b1)}
.upload-icon{left:22px;top:232px;width:78px;height:72px;background:linear-gradient(#9ab7d6,#c9a86a);border:5px solid #e9e5dc;border-radius:3px}
.upload small{position:absolute;left:76px;top:7px;font-size:12px;color:#666}
.upload strong{position:absolute;left:76px;top:23px;font-size:19px;font-weight:400;color:#444;white-space:nowrap}
.hero{left:323px;top:80px;width:486px;height:223px;background:#fff;box-shadow:0 1px 4px rgba(0,0,0,.25)}
.hero-art{left:6px;top:6px;width:474px;height:211px;background:linear-gradient(100deg,#977a5c,#b69a7a 45%,#8b6c52)}
.hero-caption{left:36px;top:34px;font-family:"Great Vibes",cursive;font-size:21px;color:#fff}
.section-title{font-size:13px;color:var(--ink)}
.gallery{left:32px;top:384px;width:766px;height:125px;background:var(--panel);border-radius:3px}
.thumb{position:absolute;top:17px;width:159px;height:92px;box-shadow:0 1px 3px rgba(0,0,0,.3)}
h2{position:absolute;font-size:17px;font-weight:400;color:var(--teal)}
.copy{position:absolute;font-size:10.2px;line-height:16.2px;text-align:justify;color:var(--text)}
.testimonials{left:577px;top:557px;width:231px;height:258px;background:var(--panel);border:1px solid #d8d0bd;box-shadow:0 1px 4px rgba(0,0,0,.2)}
.quote{position:absolute;left:12px;width:210px}
.quote .face{position:absolute;left:0;top:0;width:68px;height:64px}
.quote b{position:absolute;left:76px;top:7px;font-size:10px;font-weight:400;color:var(--ink);white-space:nowrap}
.quote p{position:absolute;left:76px;top:23px;width:135px;font-size:10px;line-height:16px;font-style:italic;color:#8a8a8a}
.steps{left:32px;top:839px;width:767px;height:127px;background:var(--panel-dark);border:1px solid #d7cfbb;border-radius:3px;overflow:hidden}
.steps-head{left:0;top:0;width:767px;height:41px;background:#f1ebdb;border-bottom:1px solid #d7cfbb}
.step{position:absolute;top:0;height:127px;border-right:1px solid #cfc7b2}
.step h3{position:absolute;top:13px;left:12px;font-size:12px;font-weight:400;color:var(--ink);white-space:nowrap}
.step h3 span{color:var(--teal);margin-left:9px}
.step h3 span.first{color:var(--red)}
.step .icon{position:absolute;top:50px;width:38px;height:36px;border-radius:3px}
.step p{position:absolute;top:100px;left:0;width:100%;text-align:center;font-size:9.5px;font-style:italic;color:#8a8a8a}
.step p.first{color:#444}
.footer{left:0;top:983px;width:828px;height:177px;background:var(--footer);border-top:2px solid #555}
.footer h4{position:absolute;top:25px;font-size:10px;font-weight:400;color:#fff}
.dots{position:absolute;top:45px;height:0;border-top:1px dotted #aaa}
.flinks li{position:absolute;list-style:none;font-size:8.3px;color:var(--footer-text);padding-left:12px}
.flinks li::before{content:"";position:absolute;left:0;top:3px;border-left:5px solid #ddd;border-top:3px solid transparent;border-bottom:3px solid transparent}
.vrule{position:absolute;top:27px;width:1px;height:120px;background:#595857}
.painting{position:absolute;width:61px;height:38px;border:1px solid #ccc}
.pay{position:absolute;top:23px;width:25px;height:16px;border-radius:2px;background:#eee;font-size:4.6px;line-height:16px;text-align:center;color:#333;overflow:hidden}
.social{position:absolute;top:93px;width:36px;text-align:center;font-size:6.5px;color:var(--footer-text)}
.social i{display:block;width:30px;height:30px;margin:0 auto 2px;border-radius:50%;background:#5d6d84}
.label{position:absolute;font-size:9.5px;color:#cfcfcf}
.bottom-bar{left:0;top:1160px;width:828px;height:40px;background:var(--footer-deep);text-align:center;line-height:40px;font-size:9.5px;color:#cfcfcf}
</style>
</head>
<body>

<div class="abs top-band"></div>

<header>
  <svg class="abs ribbon" viewBox="0 0 752 46" aria-hidden="true">
    <defs><linearGradient id="rb" x1="0" y1="0" x2="0" y2="1"><stop offset="0" stop-color="#2aafa9"/><stop offset="1" stop-color="#0e8782"/></linearGradient></defs>
    <polygon points="0,0 752,0 730,23 752,46 0,46" fill="url(#rb)"/>
  </svg>
  <div class="abs logo-mark"></div>
  <div class="abs logo-name">The Velvet Easel</div>
  <nav class="nav">
    <a class="active" href="#">Home</a>
    <a href="#" style="left:410px">About Us</a>
    <a href="#" style="left:497px">Our Gallery</a>
    <a href="#" style="left:594px">Testimonials</a>
    <a href="#" style="left:699px">Contact Us</a>
  </nav>
</header>

<ul class="quick-list">
  <li style="left:44px;top:105px">Wedding Photos</li>
  <li class="current" style="left:44px;top:131px">Child Photos</li>
  <li style="left:44px;top:158px">Pet Photos</li>
  <li style="left:44px;top:184px">Friends Photos</li>
  <li style="left:187px;top:104px">Family Photos</li>
  <li style="left:187px;top:131px">Self Photos</li>
  <li style="left:187px;top:157px">Wedding Photos</li>
  <li style="left:187px;top:183px">Child Photos</li>
</ul>

<a class="abs upload" href="#"><small>Click Here for</small><strong>Upload your Photo</strong></a>
<div class="abs upload-icon" role="img" aria-label="Framed portrait icon on an easel stand"></div>

<section class="abs hero">
  <div class="abs hero-art" role="img" aria-label="Slide: a child's photo held beside its painted portrait on a warm brown backdrop">
    <div class="abs hero-caption">Excepteur sint occaecat cupidata</div>
  </div>
</section>
<svg class="abs" style="left:355px;top:316px" width="436" height="16" aria-hidden="true">
  <line x1="0" y1="8" x2="185" y2="8" stroke="#c9c0ab"/>
  <line x1="257" y1="8" x2="436" y2="8" stroke="#c9c0ab"/>
  <circle cx="200" cy="8" r="3.5" fill="#888"/>
  <circle cx="214" cy="8" r="4" fill="#fff" stroke="var(--teal)" stroke-width="2.5"/>
  <circle cx="229" cy="8" r="3.5" fill="#888"/>
  <circle cx="244" cy="8" r="3.5" fill="#888"/>
</svg>

<div class="abs section-title" style="left:40px;top:359px">Our Gallery</div>
<section class="abs gallery">
  <svg class="abs" style="left:10px;top:48px" width="22" height="32" aria-hidden="true"><polyline points="18,2 4,16 18,30" fill="none" stroke="#888" stroke-width="5"/></svg>
  <div class="thumb" style="left:51px;background:linear-gradient(#6d6d6d,#2e2e2e)" role="img" aria-label="Black and white portrait painting of an older man"></div>
  <div class="thumb" style="left:219px;background:linear-gradient(#d9b98c,#a87048)" role="img" aria-label="Painted portrait of a woman in a straw hat"></div>
  <div class="thumb" style="left:387px;background:linear-gradient(#a0506a,#e3c4b0)" role="img" aria-label="Painting of a baby held by its mother"></div>
  <div class="thumb" style="left:554px;background:linear-gradient(#6b4a3a,#d8d6d4)" role="img" aria-label="Painting of a wedding couple kissing"></div>
  <svg class="abs" style="left:728px;top:48px" width="22" height="32" aria-hidden="true"><polyline points="4,2 18,16 4,30" fill="none" stroke="#888" stroke-width="5"/></svg>
</section>

<main>
  <h2 style="left:21px;top:520px">Welcome to our site</h2>
  <p class="copy" style="left:21px;top:553px;width:516px">Sed ut perspiciatis unde omnis iste natus error sit voluptatem accusantium doloremque laudantium, totam rem aperiam, eaque ipsa quae ab illo inventore veritatis et quasi architecto beatae vitae dicta sunt explicabo. Nemo enim ipsam voluptatem quia voluptas sit aspernatur aut odit aut fugit, sed quia consequuntur magni dolores eos qui ratione voluptatem sequi nesciunt. Neque porro quisquam est, qui dolorem ipsum quia dolor sit amet, consectetur, adipisci velit, sed quia non numquam eius modi tempora incidunt ut labore et dolore magnam aliquam quaerat voluptatem. Ut enim ad minima veniam.</p>

  <h2 style="left:21px;top:673px">Gift Ideas</h2>
  <div class="abs" style="left:28px;top:711px;width:185px;height:91px;border:2px solid #fff;box-shadow:0 1px 3px rgba(0,0,0,.35);background:linear-gradient(90deg,#2a1a14,#6a3d28 45%,#2a1a14)" role="img" aria-label="Classical oil portrait of a young man"></div>
  <p class="copy" style="left:229px;top:706px;width:309px">Sed ut perspiciatis unde omnis iste natus error sit voluptatem accusantium doloremque laudantium, totam rem aperiam, eaque ipsa quae ab illo inventore veritatis et quasi architecto beatae vitae dicta sunt explicabo. Nemo enim ipsam voluptatem quia voluptas sit aspernatur aut odit aut fugit, sed quia consequuntur magni dolores eos qui ratione voluptatem sequi nesciunt.</p>
</main>

<aside>
  <h2 style="left:576px;top:520px">Testimonials</h2>
  <a class="abs" href="#" style="left:770px;top:528px;font-size:8.5px;color:#444;text-decoration:none">View all</a>
  <div class="abs testimonials">
    <div class="quote" style="top:16px">
      <div class="face" style="background:linear-gradient(#5a4a40,#c99080)" role="img" aria-label="Customer portrait"></div>
      <b>Nemo enim ipsam</b><p>voluptatem quia voluptas sit aspernatur autodit autfugit</p>
    </div>
    <div class="quote" style="top:96px">
      <div class="face" style="background:#555;border:6px solid #444" role="img" aria-label="Placeholder customer avatar"></div>
      <b>Nemo enim ipsam</b><p>voluptatem quia voluptas sit aspernatur autodit autfugit</p>
    </div>
    <div class="quote" style="top:175px">
      <div class="face" style="background:linear-gradient(#8a6a4a,#d4b69a)" role="img" aria-label="Customer portrait"></div>
      <b>Nemo enim ipsam</b><p>voluptatem quia voluptas sit aspernatur autodit autfugit</p>
    </div>
  </div>
</aside>

<section class="abs steps">
  <div class="abs steps-head"></div>
  <div class="step" style="left:0;width:190px">
    <h3>Step - 1<span class="first">Upload your photo</span></h3>
    <div class="icon" style="left:74px;background:linear-gradient(#6fa0d0,#c9b78f)" role="img" aria-label="Photos with a magnifier"></div>
    <p class="first">Upload your desired photo to start</p>
  </div>
  <div class="step" style="left:190px;width:192px">
    <h3>Step - 2<span>Select your size</span></h3>
    <div class="icon" style="left:78px;background:linear-gradient(#e2c88a,#3a3a3a)" role="img" aria-label="Stack of photo prints"></div>
    <p>Choose your photo size</p>
  </div>
  <div class="step" style="left:382px;width:197px">
    <h3>Step - 3<span>Select Effect</span></h3>
    <div class="icon" style="left:72px;width:60px;background:linear-gradient(#6a8ab0,#c08050)" role="img" aria-label="Landscape photos showing effects"></div>
    <p>Choose your photo effect</p>
  </div>
  <div class="step" style="left:579px;width:188px;border-right:0">
    <h3>Step - 4<span>Place your order</span></h3>
    <div class="icon" style="left:76px;width:30px;background:linear-gradient(#2f7fd0,#1a4f90)" role="img" aria-label="Blue mailbox"></div>
    <p>Place, Verify and receive your order.</p>
  </div>
</section>

<footer class="abs footer">
  <h4 style="left:26px">Quick Links</h4>
  <div class="dots" style="left:26px;width:197px"></div>
  <ul class="flinks">
    <li style="left:28px;top:57px">Main Page</li>
    <li style="left:28px;top:75px">About us</li>
    <li style="left:28px;top:93px">Upload Painting</li>
    <li style="left:28px;top:111px">Featured Art</li>
    <li style="left:28px;top:129px">Latest Work</li>
    <li style="left:127px;top:57px">Support Designs</li>
    <li style="left:127px;top:75px">Our Partners</li>
    <li style="left:127px;top:93px">Recent Blog Post</li>
    <li style="left:127px;top:111px">Our Clients</li>
    <li style="left:127px;top:129px">Contact Us</li>
  </ul>
  <div class="vrule" style="left:247px"></div>

  <h4 style="left:276px">Most Recent Paintings</h4>
  <div class="dots" style="left:276px;width:244px"></div>
  <div class="painting" style="left:276px;top:58px;background:linear-gradient(#c08a3a,#6a4a2a)" role="img" aria-label="Recent painting"></div>
  <div class="painting" style="left:355px;top:58px;background:linear-gradient(#8a6a55,#e0c8b0)" role="img" aria-label="Recent painting"></div>
  <div class="painting" style="left:434px;top:58px;background:linear-gradient(#b0b8c0,#6a7480)" role="img" aria-label="Recent painting"></div>
  <div class="painting" style="left:276px;top:107px;background:linear-gradient(#c43a2a,#e0c0a0)" role="img" aria-label="Recent painting"></div>
  <div class="painting" style="left:355px;top:107px;background:linear-gradient(#e8d0b0,#9ab8d8)" role="img" aria-label="Recent painting"></div>
  <div class="painting" style="left:434px;top:107px;background:linear-gradient(#c8d8e8,#c8a878)" role="img" aria-label="Recent painting"></div>
  <div class="vrule" style="left:538px"></div>

  <div class="label" style="left:576px;top:25px">Payments :</div>
  <div class="pay" style="left:645px">Coinvale</div>
  <div class="pay" style="left:675px">Paymint</div>
  <div class="pay" style="left:705px">Cardora</div>
  <div class="pay" style="left:735px">Checkwell</div>
  <div class="pay" style="left:765px">Vantra</div>

  <div class="label" style="left:576px;top:65px">Connect with us :</div>
  <div class="social" style="left:579px"><i></i>Friendloop</div>
  <div class="social" style="left:637px"><i></i>Chirper</div>
  <div class="social" style="left:693px"><i></i>Logbook</div>
  <div class="social" style="left:748px"><i></i>Linkwork</div>
</footer>

<div class="abs bottom-bar">Copyright © 2012 www.velveteasel.example &nbsp; All rights reserved</div>

</body>
</html>
```